LA's Newest HEMP Facial Oil and Body Oil Packaging Project

We need a packaging concept for a Hemp based facial oil and body oil. We need label design for the bottle and carton graphics. I am attaching a few reference photos. The target demographic is women between 17-35 year old. Products need to be able to stand out in crowded stores with clear calls to action.
1oz Dropper Bottle with Unit Carton - Hemp Facial Oil
4oz PET Bottle with Unit Carton - Hemp + Rose Facial Oil

```html
<!DOCTYPE html>
<html lang="en">
<head>
<meta charset="utf-8">
<title>Hemp Face Oil Carton</title>
<link rel="stylesheet" href="https://fonts.googleapis.com/css2?family=Cinzel:wght@700;900&family=Caveat:wght@500;600&display=swap">
<style>
  :root {
    --page: #ffffff;
    --petal-pink: #fd9dc6;
    --rose-red: #e12f5a;
    --leaf-green: #0a9446;
    --sun-yellow: #fad840;
    --sun-yellow-deep: #f7c844;
    --tangerine: #f39320;
    --apricot: #f8b643;
    --apricot-deep: #f7ad45;
    --label-white: #ffffff;
  }
  * { margin: 0; padding: 0; box-sizing: border-box; }
  html, body {
    width: 1200px;
    height: 1200px;
    overflow: hidden;
    background: var(--page);
  }
  .canvas {
    position: relative;
    width: 1200px;
    height: 1200px;
  }
  .carton {
    position: absolute;
    left: 410px;
    top: 91px;
    width: 379px;
    height: 1018px;
    overflow: hidden;
  }
  .carton__floral {
    position: absolute;
    left: 0; top: 0;
    width: 100%;
    height: 384px;
    background:
      radial-gradient(circle at 78% 72%, rgba(225, 47, 90, 0.55) 0 22%, transparent 23%),
      radial-gradient(circle at 20% 75%, rgba(225, 47, 90, 0.45) 0 12%, transparent 13%),
      radial-gradient(circle at 14% 10%, rgba(225, 47, 90, 0.45) 0 14%, transparent 15%),
      var(--petal-pink);
  }
  .carton__title-panel {
    position: absolute;
    left: 0; top: 384px;
    width: 100%;
    height: 321px;
    background: linear-gradient(to bottom, var(--sun-yellow) 0%, var(--sun-yellow) 45%, var(--sun-yellow-deep) 100%);
  }
  .carton__brand {
    position: absolute;
    left: 0; right: 0;
    top: 30px;
    text-align: center;
    font-family: "Cinzel", "Times New Roman", serif;
    font-weight: 900;
    font-size: 78px;
    line-height: 1;
    letter-spacing: 1px;
    color: var(--tangerine);
  }
  .carton__product {
    position: absolute;
    left: 0; right: 0;
    top: 158px;
    text-align: center;
    font-family: "Caveat", "Comic Sans MS", cursive;
    font-weight: 600;
    font-size: 104px;
    line-height: 1;
    color: var(--rose-red);
  }
  .carton__ingredients {
    position: absolute;
    left: 0; top: 705px;
    width: 100%;
    height: 113px;
    background: var(--tangerine);
    display: flex;
    flex-direction: column;
    align-items: center;
    justify-content: center;
    font-family: "Caveat", "Comic Sans MS", cursive;
    font-weight: 500;
    font-size: 48px;
    line-height: 0.95;
    color: var(--rose-red);
    text-align: center;
  }
  .carton__ingredients .line-two { margin-right: 20px; }
  .carton__details {
    position: absolute;
    left: 0; top: 818px;
    width: 100%;
    height: 200px;
    background: linear-gradient(to bottom, var(--apricot) 0%, var(--apricot-deep) 100%);
    color: var(--label-white);
    font-family: Arial, Helvetica, sans-serif;
    text-align: center;
  }
  .carton__skin {
    position: absolute;
    left: 0; right: 0;
    top: 45px;
    font-size: 33px;
    letter-spacing: 0.5px;
  }
  .carton__volume {
    position: absolute;
    left: 0; right: 0;
    top: 121px;
    font-size: 27px;
  }
</style>
</head>
<body>
  <main class="canvas">
    <section class="carton">
      <div class="carton__floral" role="img" aria-label="Illustration of red roses and green leaves on a pink background"></div>

      <div class="carton__title-panel">
        <h1 class="carton__brand">HEMP</h1>
        <p class="carton__product">face oil</p>
      </div>

      <div class="carton__ingredients">
        <span class="line-one">With Hemp Oil</span>
        <span class="line-two">and Rose</span>
      </div>

      <div class="carton__details">
        <p class="carton__skin">ALL SKIN TYPES</p>
        <p class="carton__volume">1 fl. Oz 30 ml</p>
      </div>
    </section>
  </main>
</body>
</html>
```